Swimming Pool Supply Company Business Cards

We need business cards designed for company. These need to be easy to edit so that we can fill in names, titles, and contact info for each person who works here.

Dalton R. Whitfield
Manager of Legal & Finance
K.L. Brisbane, Incorporated

4837 Grenway Avenue
Marlow Heights, PA 19243

E. dalton@klbrisbane-example.com
M. (215) 555-0173
O. (215) 555-0148

Contact Information for Business Card

Looking to upgrade current business cards with graphic that can be edited. Looking for fresh ideas for an age old industry.

Font styles to use
Serif
Sans Serif

Colors

Designer to choose colors to be used in the design.

Requirements
Must have
• Professional, fresh, unique but professional

```html
<!DOCTYPE html>
<html lang="en">
<head>
<meta charset="utf-8">
<title>K.L. Brisbane Business Card</title>
<link href="https://fonts.googleapis.com/css2?family=Lato:wght@400;700;900&family=Open+Sans:wght@400;600;700&display=swap" rel="stylesheet">
<style>
  :root {
    --brand-blue: #3161a8;
    --ink: #1e1e1e;
    --muted: #555555;
    --rule: #444444;
    --paper: #ffffff;
  }
  html, body {
    margin: 0;
    padding: 0;
    width: 1200px;
    height: 1200px;
    overflow: hidden;
    background: var(--paper);
  }
  .canvas {
    position: relative;
    width: 1200px;
    height: 1200px;
  }
  .card-front {
    position: absolute;
    left: 182px;
    top: 74px;
    width: 840px;
    height: 484px;
    background: var(--brand-blue);
    color: var(--paper);
    text-align: center;
  }
  .front-wordmark {
    position: absolute;
    left: 0;
    right: 0;
    top: 160px;
    margin: 0;
    font-family: "Open Sans", sans-serif;
    font-weight: 700;
    font-size: 112px;
    line-height: 1;
    letter-spacing: 2px;
  }
  .front-tagline {
    position: absolute;
    left: 0;
    right: 0;
    top: 300px;
    margin: 0;
    font-family: "Open Sans", sans-serif;
    font-weight: 400;
    font-size: 29px;
  }
  .back-brand {
    position: absolute;
    left: 228px;
    top: 815px;
    width: 340px;
    text-align: center;
    color: var(--brand-blue);
  }
  .back-wordmark {
    margin: 0;
    font-family: "Open Sans", sans-serif;
    font-weight: 700;
    font-size: 60px;
    line-height: 1;
    letter-spacing: 1px;
  }
  .back-tagline {
    margin: 10px 0 0;
    font-family: "Open Sans", sans-serif;
    font-weight: 700;
    font-size: 11.5px;
    letter-spacing: 1.3px;
  }
  .divider {
    position: absolute;
    left: 598px;
    top: 719px;
    width: 1.5px;
    height: 265px;
    background: var(--rule);
  }
  .identity {
    position: absolute;
    right: 270px;
    top: 708px;
    text-align: right;
    font-family: "Lato", sans-serif;
  }
  .person-name {
    margin: 0;
    font-size: 37px;
    font-weight: 400;
    color: var(--ink);
    line-height: 1.15;
  }
  .person-name strong { font-weight: 900; }
  .person-role {
    margin: 0;
    font-size: 16px;
    color: var(--muted);
    line-height: 20px;
    text-align: left;
    padding-left: 72px;
  }
  .contact-list {
    position: absolute;
    left: 681px;
    top: 0;
    margin: 0;
    padding: 0;
    list-style: none;
    font-family: "Open Sans", sans-serif;
    font-weight: 600;
    font-size: 14px;
    color: var(--ink);
  }
  .contact-item {
    position: absolute;
    left: 0;
    display: flex;
    align-items: center;
    white-space: nowrap;
    line-height: 19px;
  }
  .contact-icon {
    width: 29px;
    height: 29px;
    flex: none;
    margin-right: 14px;
  }
  .bottom-band {
    position: absolute;
    left: 182px;
    top: 1098px;
    width: 839px;
    height: 19px;
    background: var(--rule);
  }
</style>
</head>
<body>
<main class="canvas">
  <section class="card-front">
    <h1 class="front-wordmark">BRISBANE</h1>
    <p class="front-tagline">Big Enough to Serve You, Small Enough to Care</p>
  </section>

  <section class="card-back">
    <div class="back-brand">
      <p class="back-wordmark">BRISBANE</p>
      <p class="back-tagline">SWIMMING POOLS, SUPPLIES &amp; ACCESSORIES</p>
    </div>

    <div class="divider"></div>

    <div class="identity">
      <h2 class="person-name"><strong>Dalton</strong> R. Whitfield</h2>
      <p class="person-role">Manager of Legal &amp; Finance</p>
      <p class="person-role">K.L. Brisbane, Incorporated</p>
    </div>

    <ul class="contact-list">
      <li class="contact-item" style="top:832px">
        <svg class="contact-icon" viewBox="0 0 29 29" aria-hidden="true">
          <rect width="29" height="29" rx="5" fill="var(--brand-blue)"/>
          <path d="M14.5 6.5a5.5 5.5 0 0 0-5.5 5.5c0 4 5.5 10.5 5.5 10.5s5.5-6.5 5.5-10.5a5.5 5.5 0 0 0-5.5-5.5z" fill="#fff"/>
          <circle cx="14.5" cy="12" r="2" fill="var(--brand-blue)"/>
        </svg>
        <span>4837 Grenway Avenue<br>Marlow Heights, PA 19243</span>
      </li>
      <li class="contact-item" style="top:872px">
        <svg class="contact-icon" viewBox="0 0 29 29" aria-hidden="true">
          <rect width="29" height="29" rx="5" fill="var(--brand-blue)"/>
          <path d="M6 12c0-2 3.5-3.5 8.5-3.5S23 10 23 12v1.5h-4v-2h-9v2H6z" fill="#fff"/>
          <path d="M10 14h9l2.5 6.5h-14z" fill="#fff"/>
          <circle cx="14.5" cy="17" r="1.6" fill="var(--brand-blue)"/>
        </svg>
        <span>(215) 555-0148</span>
      </li>
      <li class="contact-item" style="top:915px">
        <svg class="contact-icon" viewBox="0 0 29 29" aria-hidden="true">
          <rect width="29" height="29" rx="5" fill="var(--brand-blue)"/>
          <rect x="7" y="9.5" width="15" height="10.5" fill="none" stroke="#fff" stroke-width="1.4"/>
          <path d="M7 9.5l7.5 6 7.5-6M7 20l5.5-5M22 20l-5.5-5" fill="none" stroke="#fff" stroke-width="1.2"/>
        </svg>
        <span>dalton@klbrisbane-example.com</span>
      </li>
      <li class="contact-item" style="top:956px">
        <svg class="contact-icon" viewBox="0 0 29 29" aria-hidden="true">
          <rect width="29" height="29" rx="5" fill="var(--brand-blue)"/>
          <rect x="10" y="6" width="9" height="17" rx="1.5" fill="none" stroke="#fff" stroke-width="1.5"/>
          <circle cx="14.5" cy="20.3" r="0.9" fill="#fff"/>
        </svg>
        <span>(215) 555-0173</span>
      </li>
    </ul>
  </section>

  <div class="bottom-band"></div>
</main>
</body>
</html>
```